KRT Design Business Card

I need to develop a business card for my real estate design and investment company. Something clean, classic and professional with a modern vibe.

Industry/Entity Type

Real Estate

Font styles to use
Serif
Sans Serif

```html
<!DOCTYPE html>
<html lang="en">
<head>
<meta charset="UTF-8">
<title>KRT Design Business Card</title>
<link href="https://fonts.googleapis.com/css2?family=Poppins:wght@300;400&family=Roboto:wght@500;700&display=swap" rel="stylesheet">
<style>
  :root {
    --navy: #131833;
    --paper: #e9e8f5;
    --white: #ffffff;
    --backdrop: #d9d7de;
  }
  html, body {
    margin: 0;
    width: 1200px;
    height: 913px;
    overflow: hidden;
    background: var(--backdrop);
  }
  .stage { position: relative; width: 1200px; height: 913px; }
  .card {
    position: absolute;
    width: 560px;
    height: 320px;
    overflow: hidden;
    background: var(--paper);
    box-shadow: 0 10px 28px rgba(0,0,0,.25);
    font-family: "Poppins", sans-serif;
  }
  .card-front { left: 70px; top: 120px; }
  .card-back { left: 570px; top: 470px; }
  .card-shapes { position: absolute; inset: 0; }

  .brand-name {
    position: absolute;
    font-family: "Poppins", sans-serif;
    font-weight: 300;
    letter-spacing: 2px;
    white-space: nowrap;
  }
  .card-front .brand-name { left: 150px; top: 48px; font-size: 34px; color: var(--navy); }
  .card-back .brand-name { left: 0; right: 0; top: 92px; text-align: center; font-size: 40px; color: var(--white); }

  .holder { position: absolute; left: 150px; top: 176px; text-align: right; width: 200px; color: var(--white); font-family: "Roboto", sans-serif; }
  .holder-name { font-size: 31px; font-weight: 700; letter-spacing: 1px; line-height: 1.1; }
  .holder-role { font-size: 16px; font-weight: 500; letter-spacing: 1px; margin-top: 4px; }

  .divider { position: absolute; left: 372px; top: 150px; width: 1px; height: 70px; background: linear-gradient(var(--navy), var(--white), var(--navy)); }

  .contact { position: absolute; left: 392px; top: 138px; color: var(--white); font-size: 12px; line-height: 1.45; white-space: nowrap; }
  .contact-row { display: flex; align-items: flex-start; gap: 6px; margin-bottom: 8px; }
  .contact-row svg { flex: none; margin-top: 3px; }

  .footer-line { position: absolute; display: flex; align-items: center; gap: 6px; font-size: 12px; color: var(--navy); white-space: nowrap; }
  .footer-email { left: 160px; top: 290px; }
  .footer-web { left: 400px; top: 290px; }
  .card-back .footer-web { left: 330px; top: 262px; font-size: 13px; }
</style>
</head>
<body>
<main class="stage">

  <section class="card card-front">
    <svg class="card-shapes" width="560" height="320" viewBox="0 0 560 320">
      <rect width="560" height="280" fill="var(--navy)"/>
      <path d="M0 0 H480 C470 80 330 150 0 162 Z" fill="var(--paper)"/>
      <path d="M488 0 C478 88 335 160 0 172" fill="none" stroke="var(--white)" stroke-width="3"/>
      <rect x="0" y="280" width="560" height="40" fill="var(--paper)"/>
      <rect x="380" y="268" width="180" height="12" fill="var(--paper)"/>
    </svg>

    <div class="brand-name">KRT Design</div>

    <div class="holder">
      <div class="holder-name">Your Name</div>
      <div class="holder-role">Designation</div>
    </div>

    <div class="divider"></div>

    <div class="contact">
      <div class="contact-row">
        <svg width="9" height="12" viewBox="0 0 9 12"><path d="M4.5 0a4.5 4.5 0 0 0-4.5 4.5C0 8 4.5 12 4.5 12S9 8 9 4.5A4.5 4.5 0 0 0 4.5 0zm0 6.3a1.8 1.8 0 1 1 0-3.6 1.8 1.8 0 0 1 0 3.6z" fill="var(--white)"/></svg>
        <span>240 Harbor View Road,<br>NS-407</span>
      </div>
      <div class="contact-row">
        <svg width="12" height="11" viewBox="0 0 12 11"><path d="M1 4c0-2 2-3 5-3s5 1 5 3H8.5V3h-5v1zM2 5h8l1 5H1z" fill="var(--white)"/></svg>
        <span>555 210 384,555 019 762</span>
      </div>
    </div>

    <div class="footer-line footer-email">
      <svg width="12" height="9" viewBox="0 0 12 9"><rect width="12" height="9" fill="var(--navy)"/><path d="M0 0l6 5 6-5" fill="none" stroke="var(--paper)" stroke-width="1"/></svg>
      <span>yourmailid@krt.com</span>
    </div>
    <div class="footer-line footer-web">
      <svg width="11" height="11" viewBox="0 0 11 11"><circle cx="5.5" cy="5.5" r="5.5" fill="var(--navy)"/><path d="M0 5.5h11M5.5 0v11" stroke="var(--paper)" stroke-width=".8"/></svg>
      <span>yourwebsitekrt.com</span>
    </div>
  </section>

  <section class="card card-back">
    <svg class="card-shapes" width="560" height="320" viewBox="0 0 560 320">
      <rect x="0" y="48" width="560" height="160" fill="var(--navy)"/>
      <rect x="0" y="216" width="560" height="6" fill="var(--navy)"/>
    </svg>

    <div class="brand-name">KRT Design</div>

    <div class="footer-line footer-web">
      <svg width="11" height="11" viewBox="0 0 11 11"><circle cx="5.5" cy="5.5" r="5.5" fill="var(--navy)"/><path d="M0 5.5h11M5.5 0v11" stroke="var(--paper)" stroke-width=".8"/></svg>
      <span>yourwebsitekrt.com</span>
    </div>
  </section>

</main>
</body>
</html>
```